Webshop Template

For our Webstore in UK we need a complete Template,
shoppingcart is Magento, the Shop is focussed on Download software,

the name: Appvaultdepot.co.uk

Check out some other good stores, like lumawerk.de

for example the Page from 

www.brenvik.co.uk or

www.lumawerk.de

www.tastenhugo.de

www.klickrabatt.de

The Logodesign which are in Consideration

http://www.artmosaiq.com/design/5520817/logo-design-by-tomasz7kv

http://www.artmosaiq.com/design/5518360/logo-design-by-luisgaviota

http://www.artmosaiq.com/design/5517245/logo-design-by-kestrel-works

http://www.artmosaiq.com/design/5516093/logo-design-by-zumbiloft

http://www.artmosaiq.com/design/5515471/logo-design-by-tivaro

http://www.artmosaiq.com/design/5514902/logo-design-by-blue-fern-graphics-

Target Market(s)

B2C - Consumer Marcet

Industry/Entity Type

Shop

```html
<!DOCTYPE html>
<html lang="en">
<head>
<meta charset="utf-8">
<title>App Vault Depot – Webshop Template</title>
<link rel="stylesheet" href="https://fonts.googleapis.com/css2?family=Source+Sans+3:wght@400;600&display=swap">
<style>
:root{
  --red:#c0050f;
  --red-dark:#9e0009;
  --ink:#333;
  --muted:#666;
  --line:#d8d8d8;
  --page:#f2f2f2;
  --footer:#e6e6e6;
  --footer-strip:#d6d6d6;
  --btn-grey:#8d8d8d;
  --btn-dark:#1f1f1f;
}
*{box-sizing:border-box;margin:0;padding:0}
html,body{width:995px;height:1200px;overflow:hidden}
body{font-family:"Source Sans 3",sans-serif;color:var(--ink);background:var(--page);position:relative}
.abs{position:absolute}
.sheet{left:90px;top:8px;width:822px;height:991px;background:#fff;box-shadow:0 0 4px rgba(0,0,0,.2)}
.logo{left:120px;top:46px;font-size:25px;color:var(--red);letter-spacing:-.2px;white-space:nowrap}
.call{left:767px;top:21px;width:152px;height:29px;border:1px solid var(--line);background:#fff;font-size:10.5px;color:var(--muted);padding:5px 4px;white-space:nowrap}
.call b{font-weight:400;font-size:13.5px;color:#555}
.toplinks{left:545px;top:64px;font-size:10.5px;color:#555;display:flex;gap:11px;white-space:nowrap}
.toplinks span.sep{color:#999}
.search{left:688px;top:98px;width:217px;height:17px;border:1px solid #ccc;border-radius:9px;background:#f7f7f7;font-size:9.5px;color:#555;padding:1px 14px}
.search svg{position:absolute;right:8px;top:3px}
.nav{left:82px;top:124px;width:835px;height:34px;background:linear-gradient(#c90a14,var(--red-dark));border-radius:3px;display:flex;padding-left:34px}
.nav a{flex:none;color:#fff;text-decoration:none;font-size:11.6px;line-height:34px;text-align:center;white-space:nowrap;border-right:1px solid rgba(255,255,255,.25)}
.nav a:last-child{border:none}
.hero-frame{left:100px;top:166px;width:801px;height:289px;border:2px solid #e4e4e4}
.hero-in{left:102px;top:168px;width:797px;height:285px;background:radial-gradient(ellipse at 55% 10%,#5a5a5a,#1e1e1e 60%,#111)}
.hero-title{left:133px;top:233px;font-weight:400;font-size:19px;color:#fff;white-space:nowrap}
.hero-text{left:136px;top:271px;width:290px;font-size:10.5px;line-height:20px;color:#ddd}
.learn{left:300px;top:371px;width:116px;height:34px;border-radius:17px;background:linear-gradient(#f1f1f1,#cfcfcf);font-size:13px;color:#333;line-height:34px;text-align:center;white-space:nowrap}
.dots{left:117px;top:424px;display:flex;gap:4px}
.dots i{width:12px;height:12px;border-radius:2px;background:#888}
.dots i:first-child{background:var(--red);width:14px;height:14px;margin-top:-1px}
.boxes{left:448px;top:215px;width:422px;height:216px;border-radius:6px;background:linear-gradient(90deg,#f0b030,#a6d23a 25%,#2fb39a 50%,#6aa6dc 75%,#a8cdee)}
.welcome{left:111px;top:484px;font-size:14.5px;font-weight:400;white-space:nowrap}
.welcome b{color:var(--red);font-weight:400}
.intro{left:115px;top:518px;width:550px;font-size:10.2px;line-height:15px;color:#444}
.intro p{margin-bottom:15px}
.viewmore{left:601px;top:649px;font-size:9.5px;color:var(--red)}
.tab{top:692px;height:37px;width:133px;border:1px solid var(--line);border-bottom:none;border-radius:5px 5px 0 0;background:#fff;font-size:11.5px;color:#555;text-align:center;line-height:37px}
.tab.on{background:var(--red);color:#fff;border-color:var(--red)}
.panel{left:111px;top:728px;width:556px;height:249px;border:1px solid var(--line);border-radius:0 6px 6px 6px;background:linear-gradient(#fff,#f7f7f7)}
.thumb{top:757px;width:158px;height:87px;border:1px solid #bbb;border-radius:5px}
.card-text{top:855px;width:170px;font-size:9.3px;line-height:15px;color:#666}
.card-text .meta{color:#555}
.btn{top:925px;height:25px;font-size:11px;color:#fff;text-align:center;line-height:25px;border-radius:2px;white-space:nowrap}
.btn.details{width:61px;background:var(--btn-grey)}
.btn.dl{width:91px;background:var(--red)}
.cats{left:680px;top:483px;width:224px;height:238px;background:#fff;box-shadow:0 0 3px rgba(0,0,0,.15)}
.cats h2{height:33px;background:var(--red);color:#fff;font-weight:400;font-size:14.5px;line-height:33px;padding-left:17px}
.cats ul{list-style:none;padding:9px 0 0 22px}
.cats li{font-size:10px;color:#555;height:21.6px;white-space:nowrap}
.cats li::before{content:"›";color:#777;margin-right:10px;font-size:12px}
.cats .more{position:absolute;right:26px;top:213px;font-size:9.5px;color:var(--red)}
.cats .base{position:absolute;left:0;bottom:0;width:100%;height:7px;background:var(--red)}
.promo{left:678px;width:226px;border:1px solid var(--line);border-radius:5px;background:#fff}
.promo-text{left:778px;top:743px;width:118px;font-size:9.3px;line-height:15px;color:#555}
.red-link{left:778px;top:793px;font-size:9.5px;color:var(--red);white-space:nowrap}
.dark-btn{width:112px;height:21px;border-radius:5px;background:var(--btn-dark);color:#fff;font-size:9.5px;text-align:center;line-height:21px;white-space:nowrap}
.footer{left:0;top:999px;width:995px;height:157px;background:var(--footer)}
.strip{left:0;top:1156px;width:995px;height:44px;background:var(--footer-strip)}
.signup-title{left:94px;top:1022px;font-weight:400;font-size:14.5px;color:#222;white-space:nowrap}
.signup-text{left:94px;top:1050px;width:210px;font-size:8.6px;line-height:14px;color:#333}
.email{left:94px;top:1084px;width:225px;height:23px;background:#fff;border:1px solid #e2e2e2;font-size:8.5px;font-style:italic;color:#999;padding:5px 9px}
.subscribe{left:242px;top:1115px;width:71px;height:23px;border-radius:2px;background:var(--red);color:#fff;font-size:10.5px;text-align:center;line-height:23px}
.fcol h4{font-weight:400;font-size:12px;color:#444;margin-bottom:7px}
.fcol ul{list-style:none}
.fcol li{font-size:9.5px;color:#444;height:17.4px;white-space:nowrap}
.fcol li::before{content:"›";margin-right:9px;font-size:12px;color:#666}
.social{left:90px;top:1167px;display:flex;gap:15px}
.social i{width:18px;height:18px;border-radius:2px;background:#8b8b8b}
.copy{right:74px;top:1163px;font-size:9px;color:#444;white-space:nowrap}
</style>
</head>
<body>
<div class="abs sheet"></div>

<header>
  <div class="abs logo">App Vault Depot</div>
  <div class="abs call">Call Us: <b>1 (877) 555-0142</b></div>
  <div class="abs toplinks">
    <span>🛒&#xFE0E; Shopping Cart</span><span class="sep">|</span>
    <span>▤ My Wish List</span><span class="sep">|</span>
    <span>☑ Check Out</span><span class="sep">|</span>
    <span>🔒&#xFE0E; Log Out</span>
  </div>
  <div class="abs search">Search
    <svg width="12" height="12" viewBox="0 0 12 12"><circle cx="5" cy="5" r="3.5" fill="none" stroke="#555" stroke-width="1.4"/><line x1="7.6" y1="7.6" x2="11" y2="11" stroke="#555" stroke-width="1.8"/></svg>
  </div>
  <nav class="abs nav">
    <a style="width:68px">HOME</a><a style="width:84px">ABOUT US</a><a style="width:93px">PRODUCTS</a><a style="width:85px">SERVICES</a><a style="width:67px">BLOG</a><a style="width:67px">NEWS</a><a style="width:117px">NEW RELEASED</a><a style="width:87px">FREE TRIAL</a><a style="width:106px">CONTACT US</a>
  </nav>
</header>

<section class="hero">
  <div class="abs hero-frame"></div>
  <div class="abs hero-in"></div>
  <h1 class="abs hero-title">Lead Selling&nbsp; Software</h1>
  <p class="abs hero-text">Brightlane eSolutions is specialized in handling advanced web projects and the ongoing projects that require permanent maintenance and support.We like challenges and do complete these challenge with expertise.</p>
  <div class="abs learn">LEARN MORE &nbsp;❯</div>
  <div class="abs dots"><i></i><i></i><i></i><i></i><i></i></div>
  <div class="abs boxes" role="img" aria-label="Row of four colourful software boxes"></div>
</section>

<section class="welcome-area">
  <h2 class="abs welcome">Welcome to&nbsp; <b>APP VAULT DEPOT</b></h2>
  <div class="abs intro">
    <p>Lorem Ipsum is simply dummy text of the printing and typesetting industry. Lorem Ipsum has been the industry's standard dummy text ever since the 1500s, when an unknown printer took a galley of type and scrambled it to make a type specimen book. It has survived not only five centuries, but also the leap into electronic typesetting, remaining essentially unchanged.</p>
    <p>It was popularised in the 1960s with the release of Letraset Lorem Ipsum is simply dummy text of the printing and typesetting industry. Lorem Ipsum has been the industry's standard dummy text.Lorem Ipsum is simply dummy text of the printing and typesetting industry. Lorem Ipsum has been the industry's standard dummy text ever since the 1500s, when an unknown printer took a galley of type and scrambled it to make a type specimen book. It has survived not only five centuries, but also the leap into electronic typesetting, remaining essentially unchanged.</p>
  </div>
  <div class="abs viewmore">View More &gt;&gt;</div>
</section>

<section class="products">
  <div class="abs panel"></div>
  <div class="abs tab on" style="left:112px">Recommend</div>
  <div class="abs tab" style="left:250px">Top Download</div>
  <div class="abs tab" style="left:388px">New Updated</div>
  <div class="abs tab" style="left:526px">Top Freeware</div>

  <div class="abs thumb" style="left:128px;background:linear-gradient(#fff,#e8eef5)" role="img" aria-label="Software box with disc"></div>
  <div class="abs thumb" style="left:312px;background:linear-gradient(90deg,#fff,#c8d4ea 40%,#c44a3a 60%,#fff)" role="img" aria-label="Media software box"></div>
  <div class="abs thumb" style="left:495px;background:linear-gradient(#3a2a1a,#7a5530 50%,#2a1e12)" role="img" aria-label="Online radio broadcasting software banner"></div>

  <div class="abs card-text" style="left:128px">Uenim ad minim veniam, quis nostrud laboris nisi utaliquip ex irurdolor into<br><span class="meta">Categories:&nbsp; Media Management<br>Downloads:&nbsp; 84,119</span></div>
  <div class="abs card-text" style="left:311px">Uenim ad minim veniam, quis nostrud laboris nisi utaliquip ex irurdolor into<br><span class="meta">Categories:&nbsp; Media Management<br>Downloads:&nbsp; 84,119</span></div>
  <div class="abs card-text" style="left:494px">Uenim ad minim veniam, quis nostrud laboris nisi utaliquip ex irurdolor into<br><span class="meta">Categories:&nbsp; Media Management<br>Downloads:&nbsp; 84,119</span></div>

  <div class="abs btn details" style="left:127px">Details</div>
  <div class="abs btn dl" style="left:202px">Download Now</div>
  <div class="abs btn details" style="left:310px">Details</div>
  <div class="abs btn dl" style="left:385px">Download Now</div>
  <div class="abs btn details" style="left:493px">Details</div>
  <div class="abs btn dl" style="left:568px">Download Now</div>
</section>

<aside>
  <div class="abs cats">
    <h2>Categories</h2>
    <ul>
      <li>TableMatch 1.2.0GPL</li>
      <li>Quiet Pond Screensaver 2.0</li>
      <li>TaskOrbit 1.0.34</li>
      <li>SpellNest 1.0.0.0</li>
      <li>Kin Branches 0.1.0.0 Beta</li>
      <li>Restorix Music File Recovery 6.8.0.0</li>
      <li>Veltro Lite Desktop Edition -</li>
      <li>Zentrik powerbooster 3.0.7</li>
    </ul>
    <div class="more">MORE &nbsp;&gt;&gt;</div>
    <div class="base"></div>
  </div>

  <div class="abs promo" style="top:735px;height:125px"></div>
  <div class="abs" style="left:692px;top:742px;width:75px;height:110px;background:linear-gradient(135deg,#3a3a3a,#0b0b0b 60%,#2a4f7a)" role="img" aria-label="Black dictation software box"></div>
  <div class="abs promo-text">Uenim ad minim veniam, quis nostrud laboris nisi utaliquip ex irurdolor into</div>
  <div class="abs red-link">DOWNLOAD NOW &nbsp;&gt;&gt;</div>
  <div class="abs dark-btn" style="left:782px;top:818px">PURCHASE EDITION</div>

  <div class="abs promo" style="top:869px;height:108px"></div>
  <div class="abs" style="left:686px;top:871px;width:182px;height:104px;background:linear-gradient(90deg,#d9e3ee,#f4f4f4 40%,#e0e6ec)" role="img" aria-label="Software screenshot with feather quill"></div>
  <div class="abs dark-btn" style="left:782px;top:935px">CLICK HERE &gt;&gt;</div>
</aside>

<footer>
  <div class="abs footer"></div>
  <div class="abs strip"></div>
  <h3 class="abs signup-title">Sign Up to Stay in Touch</h3>
  <p class="abs signup-text">Please enter your email address below to sign up for our mailing list.</p>
  <div class="abs email">your email address here..</div>
  <div class="abs subscribe">Subscribe ›</div>
  <div class="abs fcol" style="left:443px;top:1015px">
    <h4>PRODUCTS</h4>
    <ul><li>Nunc varius eros</li><li>Sed velit quis</li><li>arcu orne laoreet.</li><li>Curabitur luctus</li><li>Intege ornare</li></ul>
  </div>
  <div class="abs fcol" style="left:609px;top:1015px">
    <h4>SUPPORT</h4>
    <ul><li>Nunc varius eros</li><li>Sed velit quis</li><li>arcu orne laoreet.</li><li>Curabitur luctus</li><li>Intege ornare</li></ul>
  </div>
  <div class="abs fcol" style="left:776px;top:1015px">
    <h4>SERVICES</h4>
    <ul><li>Nunc varius eros</li><li>Sed velit quis</li><li>arcu orne laoreet.</li><li>Curabitur luctus</li><li>Intege ornare</li></ul>
  </div>
  <div class="abs social"><i></i><i></i><i></i><i></i><i></i></div>
  <div class="abs copy">© 2013 appvaultdepot.co.uk.&nbsp;&nbsp; All right reserved</div>
</footer>
</body>
</html>
```